Business / Discount Card

Looking to create a 2 sided business card. Front side to say "Thanks for flying with Skyward Drifts" then have link to "In-Flight Photos, www.skywarddrifts-example.com.au, password: skyward" Back side of card to have company logo, phone number, facebook & instagram logo and #skywarddrifts. Also included on this side will be discount text "Book again and save 10%. Use discount code: skyward10"Round Corner Card Templates are attached. Please ensure dimensions are correct.Thanks,

Font styles to use
Sans Serif

Colors
33a6d7
ffffff
000000

Requirements
Must have
• Logo
• Blue, White and Black color scheme

```html
<!DOCTYPE html>
<html lang="en">
<head>
<meta charset="utf-8">
<title>Skyward Drifts – Business / Discount Card</title>
<link rel="stylesheet" href="https://fonts.googleapis.com/css2?family=Josefin+Sans:wght@400;600;700&display=swap">
<style>
  :root{
    --sky:#33a6d7;
    --ink:#0b0b0c;
    --paper:#ffffff;
    --paper-soft:#f1f1f2;
    --stage:#3c3c3e;
  }
  *{box-sizing:border-box;margin:0;padding:0}
  html,body{width:1200px;height:1021px;overflow:hidden}
  body{background:var(--stage);font-family:"Josefin Sans",sans-serif;position:relative}

  .card{position:absolute;left:220px;width:760px;height:434px;border-radius:34px;overflow:hidden;background:var(--ink);box-shadow:0 14px 30px rgba(0,0,0,.45)}
  .card--thanks{top:46px}
  .card--contact{top:541px}

  /* thanks side */
  .mark-placeholder{position:absolute;left:70px;top:62px;width:290px;height:290px;border-radius:50%;background:radial-gradient(circle at 40% 40%,var(--paper) 0 38%,var(--sky) 39% 100%)}
  .thanks{position:absolute;right:56px;top:120px;text-align:right;color:var(--sky);font-weight:700;font-size:29px;line-height:1.2}
  .photos{position:absolute;right:56px;top:250px;text-align:center;color:var(--paper);font-size:20px;line-height:1.3;width:330px}
  .photos .url{font-weight:700;font-size:18px}
  .photos .url span{color:var(--sky)}

  /* contact side */
  .brand{position:absolute;left:0;right:0;top:58px;text-align:center;color:var(--sky);font-weight:700;font-size:76px;letter-spacing:1px}
  .brand .dot{display:inline-block;width:40px;height:40px;border-radius:50%;background:var(--paper);vertical-align:middle;margin-left:16px;position:relative;top:-6px}
  .band{position:absolute;left:0;right:0;top:200px;height:136px;background:var(--sky);display:flex;align-items:center}
  .band-item{flex:1;display:flex;flex-direction:column;align-items:center;gap:10px;color:var(--paper);font-size:24px;height:96px;justify-content:center}
  .band-item + .band-item{border-left:2px solid rgba(255,255,255,.8)}
  .icon-square{width:24px;height:24px;border:2.5px solid var(--paper);border-radius:6px}
  .offer{position:absolute;left:0;right:0;bottom:0;height:98px;background:var(--paper-soft);display:flex;align-items:center;justify-content:center;font-size:25px;color:var(--ink)}
  .offer strong{color:var(--sky);font-weight:700;margin:0 6px}
</style>
</head>
<body>
  <section class="card card--thanks">
    <div class="mark-placeholder" role="img" aria-label="Decorative hot air balloon emblem in blue and white"></div>
    <p class="thanks">Thanks for flying<br>with Skyward Drifts</p>
    <div class="photos">
      <p>In-Flight Photos</p>
      <p class="url">www.<span>skywarddrifts-example</span>.com.au</p>
      <p>password: skyward</p>
    </div>
  </section>

  <section class="card card--contact">
    <h1 class="brand">Skyward Drifts<span class="dot"></span></h1>
    <div class="band">
      <div class="band-item">
        <svg width="22" height="22" viewBox="0 0 24 24" aria-hidden="true"><path fill="#fff" d="M6.6 10.8a15.1 15.1 0 0 0 6.6 6.6l2.2-2.2a1 1 0 0 1 1-.25 11.4 11.4 0 0 0 3.6.57 1 1 0 0 1 1 1V20a1 1 0 0 1-1 1A17 17 0 0 1 3 4a1 1 0 0 1 1-1h3.5a1 1 0 0 1 1 1c0 1.25.2 2.45.57 3.57a1 1 0 0 1-.25 1z"/></svg>
        <span>(555) 014-2290</span>
      </div>
      <div class="band-item">
        <span class="icon-square"></span>
        <span>#skywarddrifts</span>
      </div>
      <div class="band-item">
        <span class="icon-square"></span>
        <span>/skywarddrifts</span>
      </div>
    </div>
    <p class="offer">Book again and <strong>SAVE 10%</strong> - Use discount code: <strong>skyward10</strong></p>
  </section>
</body>
</html>
```